A professional business to business web site for a contract agency called VANTOMER.

We need a very clean, very professional web site created for business to business. It is an informational web site with 3 pages. We are a company that offers contract employee placements into primarily the pharmaceutical industry. I have attached a file that describes the company more fully.
Updates

Hi,

I'm sorry if I wasn't clear, but I need to have the HTML pages created so I can just upload the files you give me to the web hosting site.

Please let me know if you have any questions.

Thanks for working on my project!

Hello,

I didn't put this in the description, but I would need the web site set up on the web hosting site as well.  The web hosting site is bluepinecrest.  I want a copy of all the files as well.

Thanks,
Milo

Reason: I'm sorry, unexpectedly, I have been very busy and I haven't been able to devote the time necessary for this. I am extending the deadline by 10 days. Thank you for your patience. Thanks.

Reason: Hi everyone, I apologize again, but everything has been so busy here that I haven't been able to give this attention. I plan to work on this over the next few days. Thanks and sorry again, Milo.

Reason: I'm sorry this is taking longer than planned. I have been extremely busy. I have increased the budget on this project. Thanks.

Target Market(s)

Large professional corporations mainly in the pharmaceutical industry. The audience is hiring decisions makers within the companies and potential job candidates/job seekers.

Industry/Entity Type

Pharmaceutical

Font styles to use
Sans Serif

Requirements
Must have
• Must have a clean look that mimics the pharmaceutical industry web sites. VERY professional.
Nice to have
• A nice picture of professional business/pharma/technical people looking like a team. Colors are listed on the attached Word document.
Should not have
• No animation. Not too busy.

```html
<!DOCTYPE html>
<html lang="en">
<head>
<meta charset="utf-8">
<title>VANTOMER – Contract Professionals</title>
<link rel="stylesheet" href="https://fonts.googleapis.com/css2?family=Lato:wght@300;400&family=Open+Sans:wght@400&family=Arimo:wght@400;700&display=swap">
<style>
  :root {
    --white: #ffffff;
    --navy: #1c2f78;
    --heading-blue: #1f4f8f;
    --ink: #111111;
    --gold: #4d3f12;
    --field: #e4e4e4;
    --field-text: #8a8a8a;
    --panel: rgba(40, 42, 46, 0.72);
    --nav-active: rgba(60, 60, 60, 0.75);
    --black: #000000;
  }
  * { box-sizing: border-box; margin: 0; padding: 0; }
  html, body { width: 1200px; height: 925px; overflow: hidden; background: var(--white); }
  body { position: relative; font-family: "Open Sans", sans-serif; color: var(--ink); }

  .brand { position: absolute; left: 36px; top: 36px; display: flex; align-items: center; gap: 8px; }
  .brand-dot { width: 22px; height: 22px; border-radius: 50%; background: var(--navy); }
  .brand-name { font-family: "Lato", sans-serif; font-weight: 400; font-size: 15px; letter-spacing: 3px; color: var(--navy); }

  .contact-info { position: absolute; left: 819px; top: 34px; font-family: "Arimo", sans-serif; color: var(--ink); }
  .contact-email { font-size: 16px; }
  .contact-email strong { font-weight: 700; }
  .contact-phone { font-size: 20px; margin-top: 2px; }
  .contact-phone strong { font-size: 26px; font-weight: 700; margin-left: 6px; letter-spacing: 0.5px; }

  .hero { position: absolute; left: 0; top: 118px; width: 1200px; height: 360px; }
  .hero-photo { position: absolute; inset: 0;
    background: linear-gradient(100deg, #c9d4da 0%, #9fb0ba 22%, #b8b3aa 45%, #6e6a66 62%, #3d3a38 80%, #5a5653 100%); }
  .hero-panel { position: absolute; left: 813px; top: 0; width: 387px; height: 360px; background: var(--panel); }
  .hero-title { position: absolute; left: 27px; top: 28px; font-family: "Arimo", sans-serif; font-weight: 400;
    font-size: 54px; line-height: 70px; color: var(--white); }

  .main-nav { position: absolute; left: 0; top: 0; height: 76px; display: flex; }
  .nav-item { position: absolute; top: 0; height: 76px; line-height: 60px; font-family: "Lato", sans-serif;
    font-weight: 300; font-size: 19px; color: var(--white); white-space: nowrap; }
  .nav-home { left: 34px; }
  .nav-services { left: 200px; }
  .nav-contact { left: 433px; width: 226px; padding-left: 49px; background: var(--nav-active); }

  .section-title { position: absolute; font-family: "Lato", sans-serif; font-weight: 300; font-size: 39px; letter-spacing: 0.5px; }
  .about-title { left: 36px; top: 548px; color: var(--heading-blue); }
  .about-text { position: absolute; left: 249px; top: 618px; width: 360px; font-size: 15px; line-height: 21.7px; color: var(--ink); }

  .drop-title { left: 815px; top: 548px; color: var(--ink); }
  .drop-title span { color: var(--gold); }
  .contact-form { position: absolute; left: 818px; top: 607px; width: 312px; }
  .field { display: block; width: 312px; border: 0; background: var(--field); font-family: "Arimo", sans-serif;
    font-size: 15px; padding: 4px 7px; color: var(--ink); resize: none; }
  .field::placeholder { color: var(--field-text); }
  .field-name { height: 31px; }
  .field-email { height: 32px; margin-top: 16px; }
  .field-message { height: 93px; margin-top: 15px; }
  .submit-button { display: block; margin-top: 13px; width: 135px; height: 46px; border: 0; background: var(--black);
    color: var(--white); font-family: "Arimo", sans-serif; font-size: 16px; }

  .copyright { position: absolute; left: 37px; top: 886px; font-family: "Arimo", sans-serif; font-size: 12px; color: var(--ink); }
</style>
</head>
<body>
  <header>
    <div class="brand">
      <span class="brand-dot"></span>
      <span class="brand-name">VANTOMER</span>
    </div>
    <div class="contact-info">
      <p class="contact-email"><strong>Email:</strong> contact.us@VANTOMER.com</p>
      <p class="contact-phone">CALL US <strong>555-301-0187</strong></p>
    </div>
  </header>

  <section class="hero">
    <div class="hero-photo" role="img" aria-label="Team of lab scientists looking together at a monitor in a pharmaceutical laboratory"></div>
    <nav class="main-nav">
      <a class="nav-item nav-home">HOME</a>
      <a class="nav-item nav-services">SERVICES OFFERED</a>
      <a class="nav-item nav-contact">CONTACT US</a>
    </nav>
    <div class="hero-panel">
      <h1 class="hero-title">SOME<br>ONE-LINE<br>TEXT<br>HERE</h1>
    </div>
  </section>

  <main>
    <h2 class="section-title about-title">ABOUT US</h2>
    <p class="about-text">VANTOMER specializes in offering contract professionals primarily to companies in pharmaceutical lab environments.&nbsp; We look for the top people and companies to work with.&nbsp; Whether you are looking for a position, or looking for a contractor, you have come to the right place.&nbsp; We work hard to put great team members together with great teams.</p>

    <h2 class="section-title drop-title">DROP US A <span>LINE</span></h2>
    <form class="contact-form">
      <input class="field field-name" type="text" placeholder="Name">
      <input class="field field-email" type="email" placeholder="Email">
      <textarea class="field field-message" placeholder="Message"></textarea>
      <button class="submit-button" type="button">SUBMIT</button>
    </form>
  </main>

  <footer class="copyright">Copyright : Vantomer&nbsp; 2014</footer>
</body>
</html>
```